Moder Business Card Design for Renewables Business

Need a business card design for my business. We collect & repurpose spent coffee ground from cafes. The cards will be made from recycled paper. Needs to fit our corporate colour scheme of white, green & brown (see logo for colour codes). Eco friendly, modern, intresting & eye catching.
This card needs to convey the message of the business and fit into its mantra of eco-friendly, sustainable etc.

Target Market(s)

Cafe Owners, Coffee Drinkers, Recycling Companies, Farmers

Industry/Entity Type

Recycling

Contact Information for Business Card

Name; Peter Halloran
Phone; 0412 386 527
e-mail; info@lumatrove.com.au
website; www.lumatrove.com.au

Font styles to use
Sans Serif
Script

Colors

Designer to choose colors to be used in the design.

Requirements
Must have
• FRONT;
• Logo, Name (Peter Halloran), phone number, e-mail address, website
• BACK;
• On the back in cursive text; 'GOOD THINGS FROM EVERY CUP'
• Small facebook & Instagram logos with text 'Lumatrove'
Should not have
• messy design

```html
<!DOCTYPE html>
<html lang="en">
<head>
<meta charset="utf-8">
<title>Lumatrove Business Card</title>
<link rel="stylesheet" href="https://fonts.googleapis.com/css2?family=Oswald:wght@600&family=Montserrat:wght@400;600;700&family=Dancing+Script:wght@500&display=swap">
<style>
  :root {
    --backdrop: #d8dcdc;
    --kraft: #b59a72;
    --kraft-edge: #a88d66;
    --brown: #5e2a12;
    --green: #6cb33f;
  }
  * { box-sizing: border-box; margin: 0; padding: 0; }
  html, body { width: 1200px; height: 1050px; overflow: hidden; }
  body {
    background: var(--backdrop);
    display: flex;
    flex-direction: column;
    align-items: center;
    justify-content: center;
    gap: 40px;
    font-family: "Montserrat", sans-serif;
    color: var(--brown);
  }
  .card {
    position: relative;
    width: 800px;
    height: 456px;
    background: var(--kraft);
    border: 1px solid var(--kraft-edge);
  }
  .brand-name {
    display: flex;
    align-items: center;
    gap: 14px;
    font-family: "Montserrat", sans-serif;
    font-weight: 600;
    font-size: 38px;
    letter-spacing: 1px;
    text-transform: uppercase;
    color: var(--brown);
    white-space: nowrap;
  }
  .brand-name__dot {
    width: 22px;
    height: 22px;
    border-radius: 50%;
    background: var(--green);
    flex: none;
  }
  /* Front */
  .card--front .brand-name {
    position: absolute;
    left: 70px;
    top: 150px;
  }
  .contact {
    position: absolute;
    left: 430px;
    top: 110px;
  }
  .contact__name {
    font-family: "Oswald", sans-serif;
    font-weight: 600;
    font-size: 38px;
    letter-spacing: 1.5px;
    text-transform: uppercase;
    margin-bottom: 22px;
    white-space: nowrap;
  }
  .contact__list { list-style: none; }
  .contact__item {
    display: flex;
    align-items: center;
    gap: 12px;
    font-size: 21px;
    line-height: 1.5;
    white-space: nowrap;
  }
  .contact__icon { width: 18px; height: 18px; flex: none; }
  .tagline {
    position: absolute;
    left: 70px;
    bottom: 46px;
    font-family: "Dancing Script", cursive;
    font-weight: 500;
    font-size: 36px;
    white-space: nowrap;
  }
  /* Back */
  .card--back {
    display: flex;
    flex-direction: column;
    align-items: center;
    justify-content: center;
    gap: 40px;
  }
  .social {
    display: flex;
    align-items: center;
    gap: 12px;
  }
  .social__badge {
    width: 28px;
    height: 28px;
    border-radius: 50%;
    border: 2px solid var(--brown);
  }
  .social__handle {
    font-weight: 700;
    font-size: 22px;
  }
</style>
</head>
<body>
  <section class="card card--front" aria-label="Card front">
    <div class="brand-name"><span class="brand-name__dot" aria-hidden="true"></span>Lumatrove</div>

    <div class="contact">
      <h1 class="contact__name">Peter Halloran</h1>
      <ul class="contact__list">
        <li class="contact__item">
          <svg class="contact__icon" viewBox="0 0 24 24" fill="none" stroke="currentColor" stroke-width="2" stroke-linecap="round" stroke-linejoin="round"><path d="M5 3h4l2 5-3 2a12 12 0 0 0 6 6l2-3 5 2v4a2 2 0 0 1-2 2A17 17 0 0 1 3 5a2 2 0 0 1 2-2z"/></svg>
          <span>0412 386 527</span>
        </li>
        <li class="contact__item">
          <svg class="contact__icon" viewBox="0 0 24 24" fill="none" stroke="currentColor" stroke-width="2" stroke-linejoin="round"><rect x="2" y="5" width="20" height="14" rx="1"/><path d="M2 6l10 7 10-7"/></svg>
          <span>info@lumatrove.com.au</span>
        </li>
        <li class="contact__item">
          <svg class="contact__icon" viewBox="0 0 24 24" fill="none" stroke="currentColor" stroke-width="2"><circle cx="12" cy="12" r="10"/><path d="M2 12h20M12 2c3 3 3 17 0 20M12 2c-3 3-3 17 0 20"/></svg>
          <span>www.lumatrove.com.au</span>
        </li>
      </ul>
    </div>

    <p class="tagline">Good Things From Every Cup</p>
  </section>

  <section class="card card--back" aria-label="Card back">
    <div class="brand-name"><span class="brand-name__dot" aria-hidden="true"></span>Lumatrove</div>
    <div class="social">
      <span class="social__badge" aria-hidden="true"></span>
      <span class="social__handle">Lumatrove</span>
    </div>
  </section>
</body>
</html>
```